VELMIT Business Card

VELMIT (www.velmitpools.example) is a veteran in the swimming pool maintenance and repair business..we have served our clients for 15 years and have a research chemist, an electrician, a plumber and a pool building contractor (in part) on staff...We want to provide a business card that has a dual purpose, that people want to keep around, that leaves people speechless in the sense that they understand the mission of and the experience level of the TEAM at VELMIT.

Target Market(s)

persons who enjoy swimming and make it a priority to swim

Industry/Entity Type

Building

Font styles to use
Serif
Sans Serif

Colors
85acd3
3176b5
95b6d8
3276b5
0355a3
0555a3
0255a3
0455a3
85abd2

Requirements
Must have
• name, title, address, email, text
Nice to have
• a die cut shape
Should not have
• cartoons, pictures of pools

```html
<!DOCTYPE html>
<html lang="en">
<head>
<meta charset="utf-8">
<title>VELMIT Business Card</title>
<link href="https://fonts.googleapis.com/css2?family=Josefin+Sans:wght@400&family=Arimo:wght@400;700&family=Tinos:wght@700&display=swap" rel="stylesheet">
<style>
  :root {
    --backdrop: #2e2e2e;
    --paper: #ffffff;
    --brand-blue: #3176b5;
    --tagline-blue: #4cb4e2;
    --band-deep: #0355a3;
    --band-mid: #3176b5;
    --band-light: #85acd3;
    --band-pale: #95b6d8;
    --name-blue: #0555a3;
    --ink-white: #ffffff;
  }
  * { margin: 0; padding: 0; box-sizing: border-box; }
  html, body {
    width: 1200px; height: 900px; overflow: hidden;
    background: var(--backdrop);
  }
  .canvas { position: relative; width: 1200px; height: 900px; }

  .card {
    position: absolute;
    width: 720px; height: 400px;
    background: var(--paper);
    overflow: hidden;
  }

  /* Back of card: brand side */
  .card--back { left: 240px; top: 30px; border-radius: 10px; }
  .card--back .brand-name {
    position: absolute; left: 0; right: 0; top: 95px;
    text-align: center;
    font-family: "Arimo", sans-serif; font-weight: 700;
    font-size: 130px; line-height: 1; letter-spacing: 4px;
    color: var(--brand-blue);
  }
  .card--back .tagline {
    position: absolute; left: 0; right: 0; top: 265px;
    text-align: center;
    font-family: "Josefin Sans", sans-serif;
    font-size: 32px; letter-spacing: 4px;
    color: var(--tagline-blue);
  }

  /* Front of card: contact side, die-cut corners */
  .card--front {
    left: 240px; top: 470px;
    border-radius: 10px 80px 10px 80px;
  }
  .card--front .wave { position: absolute; inset: 0; }
  .card--front .brand-name {
    position: absolute; left: 60px; top: 92px;
    font-family: "Arimo", sans-serif; font-weight: 700;
    font-size: 72px; line-height: 1; letter-spacing: 2px;
    color: var(--brand-blue);
  }
  .card--front .tagline {
    position: absolute; left: 48px; top: 186px;
    font-family: "Josefin Sans", sans-serif;
    font-size: 18px; letter-spacing: 2px;
    color: var(--tagline-blue);
  }
  .holder { position: absolute; right: 40px; top: 36px; text-align: right; }
  .holder__name {
    font-family: "Arimo", sans-serif; font-weight: 700;
    font-size: 27px; color: var(--name-blue); line-height: 1;
  }
  .holder__title {
    font-family: "Tinos", serif; font-weight: 700;
    font-size: 16px; color: var(--name-blue);
  }
  .address {
    position: absolute; right: 40px; top: 238px;
    display: flex; align-items: center; gap: 8px;
    font-family: "Arimo", sans-serif; font-size: 20px;
    color: var(--ink-white);
  }
  .contacts {
    position: absolute; left: 36px; bottom: 34px;
    font-family: "Arimo", sans-serif; font-size: 21px;
    color: var(--ink-white);
  }
  .contacts__row { display: flex; align-items: center; gap: 12px; line-height: 30px; }
  .icon { width: 22px; height: 22px; flex: none; }
</style>
</head>
<body>
<main class="canvas">

  <section class="card card--back">
    <div class="brand-name">VELMIT</div>
    <div class="tagline">CLEAR WATER...SKILLED CREW</div>
  </section>

  <section class="card card--front">
    <svg class="wave" viewBox="0 0 720 400" width="720" height="400" aria-hidden="true">
      <path d="M0,235 C160,330 400,260 720,110 L720,400 L0,400 Z" fill="var(--band-pale)"/>
      <path d="M0,250 C160,340 400,275 720,128 L720,400 L0,400 Z" fill="var(--paper)"/>
      <path d="M0,256 C160,346 400,285 720,140 L720,400 L0,400 Z" fill="var(--band-light)"/>
      <path d="M0,268 C160,356 410,300 720,168 L720,400 L0,400 Z" fill="var(--band-mid)"/>
      <path d="M0,276 C160,362 420,312 720,190 L720,400 L0,400 Z" fill="var(--band-deep)"/>
    </svg>

    <div class="brand-name">VELMIT</div>
    <div class="tagline">CLEAR WATER...SKILLED CREW</div>

    <div class="holder">
      <div class="holder__name">YOUR NAME</div>
      <div class="holder__title">Designation</div>
    </div>

    <div class="address">
      <span>Your address</span>
      <svg class="icon" viewBox="0 0 22 22" aria-hidden="true">
        <rect x="1" y="1" width="20" height="20" rx="3" fill="var(--ink-white)"/>
        <path d="M4,11 L11,5 L18,11 M6,10 V17 H16 V10 M9.5,17 V13 H12.5 V17" fill="none" stroke="var(--band-deep)" stroke-width="1.6"/>
      </svg>
    </div>

    <div class="contacts">
      <div class="contacts__row">
        <svg class="icon" viewBox="0 0 22 22" aria-hidden="true">
          <rect x="1" y="4" width="20" height="14" rx="2" fill="var(--ink-white)"/>
          <path d="M2,5 L11,12 L20,5" fill="none" stroke="var(--band-deep)" stroke-width="1.6"/>
        </svg>
        <span>info@velmitpools.example</span>
      </div>
      <div class="contacts__row">
        <svg class="icon" viewBox="0 0 22 22" aria-hidden="true">
          <circle cx="11" cy="11" r="10" fill="var(--ink-white)"/>
          <path d="M1,11 H21 M11,1 C6,6 6,16 11,21 M11,1 C16,6 16,16 11,21" fill="none" stroke="var(--band-deep)" stroke-width="1.4"/>
        </svg>
        <span>www.velmitpools.example</span>
      </div>
    </div>
  </section>

</main>
</body>
</html>
```